STI/STD Medical Clinic- Wellspring Crest Partners, Inc Website

We are a STI clinic in florida looking for a website. We want to be professional but also playful. We want a buildout similar to the website listed below as our clinic is very similar to theirs.

This is a great example of a clinic doing similar stuff as us. We obviously do not want their color scheme but their format and buildout work. Please see our logo attached for color schemes etc.

https://bluefernclinicmiami.org

Industry/Entity Type

Medical

Coding

Coded - Design and coding required

Number of Pages Required

5+ page

Font styles to use
Sans Serif

```html
<!DOCTYPE html>
<html lang="en">
<head>
<meta charset="utf-8">
<title>Wellspring Crest Partners – STI Clinic Confidential Services</title>
<link href="https://fonts.googleapis.com/css2?family=Poppins:ital,wght@0,400;0,500;0,600;0,700;1,400&display=swap" rel="stylesheet">
<style>
:root{
  --pink:#f23fae;
  --magenta:#e43ad0;
  --orange:#ff7a35;
  --coral:#ff5b5b;
  --blue:#1d7cf2;
  --violet:#6a3fe0;
  --indigo:#4b3bd0;
  --cream:#fdf3ee;
  --white:#ffffff;
  --ink:#2b2c3a;
  --muted:#6d6f7c;
  --night:#2c2e3c;
  --grad-warm:linear-gradient(90deg,var(--pink),var(--orange));
  --grad-cool:linear-gradient(90deg,var(--blue),var(--violet));
}
*{box-sizing:border-box;margin:0;padding:0}
html,body{width:1200px;height:4792px;overflow:hidden}
body{position:relative;background:var(--cream);font-family:"Poppins",sans-serif;color:var(--ink)}
.abs{position:absolute}
a{color:inherit;text-decoration:none}
.btn{position:absolute;display:flex;align-items:center;gap:10px;height:40px;padding:0 8px 0 22px;border-radius:20px;background:var(--blue);color:var(--white);font-size:13px;font-weight:500;letter-spacing:.2px}
.btn .ring{width:22px;height:22px;border:1.5px solid var(--white);border-radius:50%;display:flex;align-items:center;justify-content:center}
.grad-cool-text{background:var(--grad-cool);-webkit-background-clip:text;background-clip:text;color:transparent}
.grad-warm-text{background:var(--grad-warm);-webkit-background-clip:text;background-clip:text;color:transparent}
.mark{width:44px;height:44px;border-radius:50%;border:3px solid var(--violet);opacity:.55;left:578px}
.section-title{position:absolute;left:0;width:1200px;text-align:center;font-size:33px;font-weight:700;letter-spacing:.5px}
.section-sub{position:absolute;left:0;width:1200px;text-align:center;font-size:12.5px;color:var(--ink)}

/* top bar */
.topbar{left:0;top:0;width:1200px;height:34px;background:var(--grad-warm);color:var(--white);font-size:12px}
.topbar .links{left:64px;top:9px;display:flex;gap:16px}
.topbar .links span+span{border-left:1px solid rgba(255,255,255,.6);padding-left:16px}
.topbar .contact{right:62px;top:8px;display:flex;gap:20px;align-items:center;font-size:13px}
.topbar .contact span{display:flex;align-items:center;gap:8px}

/* header */
.header{left:0;top:34px;width:1200px;height:82px;background:var(--white)}
.brand{display:flex;align-items:center;gap:10px}
.brand .dot{width:30px;height:30px;border-radius:50%;background:var(--violet)}
.brand .name{font-weight:700;color:var(--blue);line-height:1}
.brand .name small{display:block;font-weight:700;letter-spacing:2px}
.header .brand{position:absolute;left:62px;top:20px}
.header .brand .name{font-size:24px}
.header .brand .name small{font-size:8.5px;margin-top:3px}
.nav{position:absolute;left:400px;top:32px;display:flex;gap:22px;font-size:13px;color:var(--ink)}
.nav .active{color:var(--pink)}
.header .btn{left:893px;top:20px;height:40px}

/* hero */
.hero-photo{left:0;top:116px;width:1200px;height:596px;background:linear-gradient(120deg,#8c8f8a,#c7a88c 40%,#a98d77 65%,#6d7a86)}
.hero-panel{left:600px;top:469px;width:600px;height:312px}
.hero-title{left:652px;top:530px;font-size:39px;line-height:48px;font-weight:700;color:var(--white);letter-spacing:-.5px}
.hero-sub{left:658px;top:634px;font-size:15px;color:var(--white)}
.hero-panel-btn{left:657px;top:671px}
.slider-arrow{position:absolute;width:44px;height:44px;border-radius:50%;display:flex;align-items:center;justify-content:center}
.slider-arrow.fill{background:var(--blue)}
.slider-arrow.line{border:2px solid var(--white)}

/* services */
.service-card{position:absolute;top:986px;width:285px;height:327px;background:var(--white);border-radius:4px;box-shadow:0 4px 18px rgba(60,40,80,.08);text-align:center}
.service-card.featured{border:2px solid #ff7a7a}
.service-card .icon{width:96px;height:96px;border-radius:50%;margin:36px auto 0;display:flex;align-items:center;justify-content:center;box-shadow:0 0 0 6px rgba(0,0,0,.04)}
.service-card h3{margin-top:24px;font-size:17px;font-weight:600}
.service-card p{margin:20px auto 0;width:225px;font-size:11.5px;line-height:20px;color:var(--muted)}
.service-card .more{display:inline-flex;align-items:center;gap:4px;margin-top:18px;font-size:12px;color:var(--violet);text-decoration:underline}
.dots{left:586px;top:1348px;display:flex;gap:4px}
.dots i{width:6px;height:8px;border:1px solid var(--coral);border-radius:2px}
.dots i:first-child{background:var(--coral)}

/* about */
.about-bg{left:0;top:1420px;width:1200px;height:610px;background:var(--white)}
.about-label{left:125px;top:1596px;font-size:11px;color:var(--blue);letter-spacing:.5px}
.about-title{left:122px;top:1612px;font-size:33px;font-weight:700;line-height:40px}
.about-group{left:124px;top:1655px;font-size:18px;color:var(--orange);font-weight:500}
.about-text{left:125px;width:350px;font-size:11.5px;line-height:19.5px;color:var(--muted)}
.about-visual{left:632px;top:1535px;width:414px;height:418px;border-radius:48% 52% 45% 55%/50% 44% 56% 50%;background:radial-gradient(circle at 50% 50%,#d9d8e4 0 48%,rgba(255,255,255,0) 49%),conic-gradient(from 30deg,var(--pink),var(--orange),var(--violet),var(--blue),var(--pink));opacity:.9}

/* sti band */
.band{left:0;top:2024px;width:1200px;height:466px}
.band-title{left:0;width:1200px;top:2152px;text-align:center;font-size:32px;font-weight:700;letter-spacing:.5px}
.band-text{left:0;width:1200px;text-align:center;color:var(--white)}

/* team */
.team-card{position:absolute;top:2703px;width:286px;height:376px;background:var(--white);border:2px solid;text-align:center}
.team-card .photo{margin:6px 6px 0;height:222px}
.team-card h3{margin-top:30px;font-size:16px;font-weight:600;color:var(--indigo)}
.team-card .role{margin-top:6px;font-size:13px;color:var(--ink)}
.team-card .loc{margin-top:28px;font-size:12.5px;color:var(--orange)}

/* reviews */
.review-photo{left:0;top:3224px;width:1200px;height:412px;background:linear-gradient(100deg,#b7aca5,#d7c5bd 45%,#c99e9c 60%,#5b6478)}
.review-panel{left:0;top:3328px;width:615px;height:366px}
.quote-mark{left:56px;top:3340px;font-size:110px;font-weight:700;color:var(--white);line-height:1;letter-spacing:-8px}
.review-title{left:58px;top:3432px;font-size:32px;font-weight:600;color:var(--white);letter-spacing:.5px}
.avatar{left:60px;top:3510px;width:78px;height:78px;border-radius:50%;border:3px solid rgba(255,255,255,.8);background:linear-gradient(160deg,#e6c3ad,#8d5d49)}
.review-text{left:157px;top:3510px;width:400px;font-size:13.5px;line-height:23px;font-style:italic;color:var(--white)}
.review-author{left:156px;top:3598px;font-size:14px;font-weight:600;color:var(--blue);display:flex;align-items:center;gap:12px}
.review-author i{width:20px;height:3px;background:var(--blue);display:block}

/* booking */
.book-photo{left:154px;top:3962px;width:354px;height:354px;border-radius:50%;padding:6px;background:linear-gradient(135deg,var(--blue),var(--violet),var(--pink))}
.book-photo div{width:100%;height:100%;border-radius:50%;border:6px solid var(--cream);background:linear-gradient(170deg,#c9c4bf,#8a6f60 55%,#5a4238)}
.field{position:absolute;height:44px;border-radius:22px;background:var(--white);box-shadow:0 3px 12px rgba(60,40,80,.07);font-size:11px;color:var(--muted);padding:13px 16px}
.field.tall{height:104px}

/* footer */
.footer{left:0;top:4436px;width:1200px;height:330px}
.footer .brand{position:absolute;left:60px;top:4515px}
.footer .brand .name{font-size:42px}
.footer .brand .name small{font-size:13px;letter-spacing:4px;margin-top:4px}
.footer-about{left:60px;top:4608px;width:258px;font-size:11px;line-height:20px;color:var(--white)}
.footer-link{left:58px;top:4681px;font-size:12.5px;color:var(--pink);text-decoration:underline;display:flex;gap:8px;align-items:center}
.footer h4{position:absolute;top:4510px;font-size:13px;font-weight:700;letter-spacing:.5px}
.sitemap{left:334px;top:4552px;font-size:11px;line-height:22.5px;color:var(--white);list-style:none}
.sitemap li{display:flex;align-items:center;gap:14px}
.sitemap li::before{content:"";width:6px;height:6px;border:1.5px solid var(--pink);border-radius:50%}
.contact-row{position:absolute;left:612px;display:flex;gap:18px;align-items:flex-start;font-size:11px;color:var(--white);line-height:18px}
.contact-row b{color:var(--blue);font-weight:400}
.social{position:absolute;top:4556px;width:40px;height:40px;border-radius:50%;background:var(--grad-warm)}
.copyright{left:0;top:4762px;width:1200px;height:30px;background:var(--grad-warm);color:var(--white);font-size:11px;text-align:center;line-height:30px}
</style>
</head>
<body>

<!-- top bar -->
<div class="abs topbar">
  <div class="abs links"><span>Patient Portal</span><span>Patient Messaging App</span></div>
  <div class="abs contact">
    <span><svg width="16" height="16" viewBox="0 0 24 24" fill="none" stroke="#fff" stroke-width="1.8"><path d="M5 3h4l2 5-3 2a11 11 0 0 0 6 6l2-3 5 2v4a2 2 0 0 1-2 2A17 17 0 0 1 3 5a2 2 0 0 1 2-2z"/></svg>Call Us : <b>305 555 0142</b></span>
    <span style="opacity:.6">|</span>
    <span><svg width="18" height="14" viewBox="0 0 24 18" fill="none" stroke="#fff" stroke-width="1.8"><rect x="1" y="1" width="22" height="16" rx="2"/><path d="M1 2l11 8 11-8"/></svg>info@wellspringcrest.com</span>
  </div>
</div>

<!-- header -->
<header class="abs header">
  <div class="brand"><span class="dot"></span><span class="name">Wellspring Crest<small>PARTNERS</small></span></div>
  <nav class="nav"><span class="active">&#9670; Home</span><span>About</span><span>Meet The Team</span><span>Services</span><span>News</span><span>Faqs</span><span>Contact</span></nav>
  <a class="btn">REQUEST AN APPOINTMENT <span class="ring"><svg width="8" height="10" viewBox="0 0 8 10"><path d="M2 1l4 4-4 4" stroke="#fff" stroke-width="1.6" fill="none"/></svg></span></a>
</header>

<!-- hero -->
<div class="abs hero-photo" role="img" aria-label="Photo of a group of smiling young friends outdoors under festival bunting"></div>
<div class="slider-arrow fill" style="left:60px;top:646px"><svg width="12" height="16" viewBox="0 0 12 16"><path d="M9 2L3 8l6 6" stroke="#fff" stroke-width="2" fill="none"/></svg></div>
<div class="slider-arrow line" style="left:110px;top:646px"><svg width="12" height="16" viewBox="0 0 12 16"><path d="M3 2l6 6-6 6" stroke="#fff" stroke-width="2" fill="none"/></svg></div>
<svg class="abs hero-panel" viewBox="0 0 600 312" preserveAspectRatio="none">
  <defs><linearGradient id="warm" x1="0" y1="1" x2="1" y2="0"><stop offset="0" stop-color="#f23fae"/><stop offset="1" stop-color="#ff7a35"/></linearGradient></defs>
  <path d="M0 0H600V284C520 268 430 298 330 296 220 294 140 284 70 300 40 306 15 306 0 304Z" fill="url(#warm)"/>
</svg>
<h1 class="abs hero-title">STI CLINIC CONFIDENTIAL<br>SERVICES &amp; SUPPORTS</h1>
<p class="abs hero-sub">The Florida Independent Sexual Health Service Clinic</p>
<a class="btn hero-panel-btn">REQUEST AN APPOINTMENT <span class="ring"><svg width="8" height="10" viewBox="0 0 8 10"><path d="M2 1l4 4-4 4" stroke="#fff" stroke-width="1.6" fill="none"/></svg></span></a>

<!-- services -->
<div class="abs mark" style="top:838px"></div>
<h2 class="section-title grad-cool-text" style="top:896px">OUR SERVICES</h2>
<p class="section-sub" style="top:941px">Lorem Ipsum has been the industry's standard dummy text ever since thes.</p>

<div class="service-card" style="left:149px">
  <div class="icon" style="background:linear-gradient(135deg,#8a3fe6,#5b2fc9)"><svg width="40" height="40" viewBox="0 0 40 40" fill="none" stroke="#fff" stroke-width="2.2"><rect x="8" y="14" width="24" height="12" rx="6" transform="rotate(-35 20 20)"/><path d="M16 11l9 13"/></svg></div>
  <h3 class="grad-warm-text">PREP</h3>
  <p>Lorem Ipsum has been the industry's standard dummy text ever since thes, when an unknown printer.</p>
  <a class="more">Read More <svg width="22" height="8" viewBox="0 0 22 8"><path d="M0 4h20M16 1l4 3-4 3" stroke="#6a3fe0" stroke-width="1.4" fill="none"/></svg></a>
</div>
<div class="service-card featured" style="left:457px">
  <div class="icon" style="background:linear-gradient(135deg,#ff7a35,#f2365e)"><svg width="40" height="40" viewBox="0 0 40 40" fill="none" stroke="#fff" stroke-width="2.2"><path d="M20 6c-4 0-6 3-6 6 0 4 4 9 14 22M20 6c4 0 6 3 6 6 0 4-4 9-14 22"/></svg></div>
  <h3 class="grad-warm-text">HIV</h3>
  <p>Lorem Ipsum has been the industry's standard dummy text ever since thes, when an unknown printer.</p>
  <a class="more">Read More <svg width="22" height="8" viewBox="0 0 22 8"><path d="M0 4h20M16 1l4 3-4 3" stroke="#6a3fe0" stroke-width="1.4" fill="none"/></svg></a>
</div>
<div class="service-card" style="left:765px">
  <div class="icon" style="background:linear-gradient(135deg,#f452c6,#d52aa8)"><svg width="40" height="40" viewBox="0 0 40 40" fill="none" stroke="#fff" stroke-width="2.2"><path d="M20 5l11 5v9c0 8-5 13-11 16-6-3-11-8-11-16v-9z"/><path d="M15 20l4 4 7-8"/></svg></div>
  <h3 class="grad-warm-text">STI</h3>
  <p>Lorem Ipsum has been the industry's standard dummy text ever since thes, when an unknown printer.</p>
  <a class="more">Read More <svg width="22" height="8" viewBox="0 0 22 8"><path d="M0 4h20M16 1l4 3-4 3" stroke="#6a3fe0" stroke-width="1.4" fill="none"/></svg></a>
</div>
<div class="abs dots"><i></i><i></i><i></i></div>

<!-- about -->
<svg class="abs" style="left:0;top:1410px" width="1200" height="40" viewBox="0 0 1200 40" preserveAspectRatio="none"><path d="M0 34C150 12 300 38 500 22 700 6 900 30 1200 14V40H0Z" fill="#fff"/></svg>
<div class="abs about-bg"></div>
<div class="abs mark" style="left:124px;top:1530px"></div>
<p class="abs about-label">ABOUT</p>
<h2 class="abs about-title grad-cool-text">WELLSPRING CREST</h2>
<p class="abs about-group">PARTNERS</p>
<p class="abs about-text" style="top:1693px">Lorem Ipsum has been the industry's standard dummy text ever since the 1500s, when an unknown printer took a galley of type and scrambled it to make a type specim book. It has survived not only five centuries.</p>
<p class="abs about-text" style="top:1786px">Lorem Ipsum has been the industry's standard dummy text ever since the 1500s, when an unknown printer took a galley of type and scrambled it to make a type specimen book. It has survived not only five centuries, but also the leap into electronic typesetting, remaining essentially unchanged.</p>
<a class="btn" style="left:125px;top:1899px">LEARN MORE <span class="ring"><svg width="8" height="10" viewBox="0 0 8 10"><path d="M2 1l4 4-4 4" stroke="#fff" stroke-width="1.6" fill="none"/></svg></span></a>
<div class="abs about-visual" role="img" aria-label="Photo of a clinician talking with a patient in an exam room, framed by colourful looping ribbons"></div>

<!-- sti band -->
<svg class="abs band" viewBox="0 0 1200 466" preserveAspectRatio="none">
  <defs><linearGradient id="cool" x1="0" y1="0" x2="1" y2="1"><stop offset="0" stop-color="#4b3bd0"/><stop offset="1" stop-color="#5a3fe0"/></linearGradient></defs>
  <path d="M0 0H1200V452C1100 466 980 440 860 446 720 454 600 470 460 456 320 444 160 440 0 460Z" fill="url(#cool)"/>
</svg>
<div class="abs mark" style="top:2094px;border-color:#fff;opacity:.4"></div>
<h2 class="abs band-title grad-warm-text">HOW DO I KNOW IF I HAVE AN STI ?</h2>
<p class="abs band-text" style="top:2204px;font-size:15px;line-height:24px">You can have an STI without knowing it. Get tested. It's the<br>only way to be sure.</p>
<p class="abs band-text" style="top:2276px;font-size:17px">Testing Is Easy And Hassle Free.</p>
<a class="btn" style="left:436px;top:2326px">CONTACT US <span class="ring"><svg width="8" height="10" viewBox="0 0 8 10"><path d="M2 1l4 4-4 4" stroke="#fff" stroke-width="1.6" fill="none"/></svg></span></a>
<a class="btn" style="left:598px;top:2326px">VIEW SERVICES <span class="ring"><svg width="8" height="10" viewBox="0 0 8 10"><path d="M2 1l4 4-4 4" stroke="#fff" stroke-width="1.6" fill="none"/></svg></span></a>

<!-- team -->
<div class="abs mark" style="top:2544px"></div>
<h2 class="section-title grad-cool-text" style="top:2604px">MEET OUR TEAM</h2>
<p class="section-sub" style="top:2652px">Lorem Ipsum has been the industry's standard dummy text ever since.</p>
<div class="team-card" style="left:149px;border-color:var(--pink)">
  <div class="photo" role="img" aria-label="Portrait of a medical provider in a white coat" style="background:linear-gradient(180deg,#fbeef6,#e9dcd4)"></div>
  <h3>MEMBER NAME</h3><p class="role">Medical Provider</p><p class="loc">Location : Florida</p>
</div>
<div class="team-card" style="left:457px;border-color:var(--blue)">
  <div class="photo" role="img" aria-label="Portrait of the executive director in a white coat" style="background:linear-gradient(180deg,#eef0fa,#dcdde6)"></div>
  <h3>MEMBER NAME</h3><p class="role">Executive Director</p><p class="loc">Location : Florida</p>
</div>
<div class="team-card" style="left:765px;border-color:var(--orange)">
  <div class="photo" role="img" aria-label="Portrait of the clinic practice manager with a stethoscope" style="background:linear-gradient(180deg,#fdf0ec,#e4e2e6)"></div>
  <h3>MEMBER NAME</h3><p class="role">Clinic Practice Manager</p><p class="loc">Location : Florida</p>
</div>
<a class="btn" style="left:517px;top:3105px">VISIT OUR TEAM <span class="ring"><svg width="8" height="10" viewBox="0 0 8 10"><path d="M2 1l4 4-4 4" stroke="#fff" stroke-width="1.6" fill="none"/></svg></span></a>

<!-- reviews -->
<div class="abs review-photo" role="img" aria-label="Photo of a smiling young woman in a pink sweater"></div>
<svg class="abs review-panel" viewBox="0 0 615 366" preserveAspectRatio="none">
  <path d="M0 0H615V356C540 340 460 360 370 350 270 340 160 356 80 346 40 340 15 342 0 346Z" fill="url(#warm)"/>
</svg>
<div class="abs quote-mark">“</div>
<h2 class="abs review-title">PATIENTS REVIEWS</h2>
<div class="abs avatar" role="img" aria-label="Photo of the reviewing patient"></div>
<p class="abs review-text">" Lorem Ipsum has been the industry's standard dummy text ever since the 1500s, when an unknown printer took a galley of type and scrambled make a "</p>
<p class="abs review-author"><i></i>Client Name</p>
<div class="slider-arrow fill" style="left:1093px;top:3546px"><svg width="12" height="16" viewBox="0 0 12 16"><path d="M9 2L3 8l6 6" stroke="#fff" stroke-width="2" fill="none"/></svg></div>
<div class="slider-arrow line" style="left:1143px;top:3546px"><svg width="12" height="16" viewBox="0 0 12 16"><path d="M3 2l6 6-6 6" stroke="#fff" stroke-width="2" fill="none"/></svg></div>

<!-- booking -->
<div class="abs mark" style="top:3760px"></div>
<h2 class="section-title grad-cool-text" style="top:3826px">BOOK AN APPOINTMENT</h2>
<p class="section-sub" style="top:3878px;font-size:14px">Want to Hear More About Wellspring Crest Partners</p>
<div class="abs book-photo" role="img" aria-label="Photo of a thoughtful young woman resting her chin on her hands"><div></div></div>
<div class="field" style="left:597px;top:3975px;width:236px">Name *</div>
<div class="field" style="left:851px;top:3975px;width:236px">Email *</div>
<div class="field" style="left:597px;top:4037px;width:236px">Phone *</div>
<div class="field" style="left:851px;top:4037px;width:236px">Discussion For * <span style="float:right;color:var(--coral)">&#9662;</span></div>
<div class="field tall" style="left:597px;top:4100px;width:490px">Message *</div>
<a class="btn" style="left:596px;top:4225px">SUBMIT <span class="ring"><svg width="8" height="10" viewBox="0 0 8 10"><path d="M2 1l4 4-4 4" stroke="#fff" stroke-width="1.6" fill="none"/></svg></span></a>

<!-- footer -->
<svg class="abs footer" viewBox="0 0 1200 330" preserveAspectRatio="none">
  <path d="M0 20C160 40 330 8 520 22 720 36 900 4 1200 24V330H0Z" fill="#2c2e3c"/>
</svg>
<div class="brand"><span class="dot"></span><span class="name">Wellspring Crest<small>PARTNERS</small></span></div>
<p class="abs footer-about">Lorem Ipsum has been the industry's standard dummy text ever since the when an unknown printer took a galley of type and.</p>
<a class="abs footer-link">REQUEST AN APPOINTMENT <svg width="16" height="16" viewBox="0 0 16 16" fill="none" stroke="#f23fae" stroke-width="1.4"><circle cx="8" cy="8" r="7"/><path d="M7 5l3 3-3 3"/></svg></a>

<h4 class="grad-warm-text" style="left:337px">SITEMAP</h4>
<ul class="abs sitemap"><li>Home</li><li>About</li><li>Meet the team</li><li>Services</li><li>News</li><li>Faq's</li><li>Contact</li></ul>

<h4 class="grad-warm-text" style="left:612px">CONTACT US</h4>
<div class="contact-row" style="top:4552px"><svg width="18" height="22" viewBox="0 0 18 22" fill="none" stroke="#f23fae" stroke-width="1.6"><path d="M9 21s7-7 7-12A7 7 0 0 0 2 9c0 5 7 12 7 12z"/><circle cx="9" cy="9" r="2.5"/></svg><span>WELLSPRING CREST<br>florida - Address city state country</span></div>
<div class="contact-row" style="top:4610px"><svg width="18" height="18" viewBox="0 0 24 24" fill="none" stroke="#f23fae" stroke-width="1.8"><path d="M5 3h4l2 5-3 2a11 11 0 0 0 6 6l2-3 5 2v4a2 2 0 0 1-2 2A17 17 0 0 1 3 5a2 2 0 0 1 2-2z"/></svg><span><b>Call Us:</b> 305.555.0142</span></div>
<div class="contact-row" style="top:4645px"><svg width="18" height="18" viewBox="0 0 20 20" fill="none" stroke="#f23fae" stroke-width="1.6"><rect x="2" y="7" width="16" height="8" rx="1"/><path d="M5 7V2h10v5M5 13h10v5H5z"/></svg><span><b>Fax Us:</b> 305.555.0143</span></div>
<div class="contact-row" style="top:4680px"><svg width="18" height="14" viewBox="0 0 24 18" fill="none" stroke="#f23fae" stroke-width="1.8"><rect x="1" y="1" width="22" height="16" rx="2"/><path d="M1 2l11 8 11-8"/></svg><span>info@wellspringcrest.com</span></div>

<h4 class="grad-warm-text" style="left:887px">FOLLOW US</h4>
<span class="social" style="left:887px" role="img" aria-label="Social profile link"></span>
<span class="social" style="left:933px" role="img" aria-label="Social profile link"></span>
<span class="social" style="left:979px" role="img" aria-label="Social profile link"></span>
<span class="social" style="left:1025px" role="img" aria-label="Social profile link"></span>

<div class="abs copyright">©WELLSPRING CREST PARTNERS - 2022 All rights reserved</div>

</body>
</html>
```